Business Card Design for a technology company

Our current business card is outdated and stale.

We need a new look and one soon.

We're a telematics (GPS tracking) company based in Australia. Our audiences are transport and logistics company.

Target Market(s)

1. Transport and Logistics Companies
2. Food and Beverage Manufacturers
3. Concrete Businesses

Industry/Entity Type

Logistics

Contact Information for Business Card

Lumen Rove

Font styles to use
Sans Serif

Colors
3276b5
0255a3
85acd3
cfdeed
ffffff

Requirements
Must have
• Logo
• "Premium Suppliers of Real Time Temperature Tracking"
• Contact Name
• Business Title
• Address
• Telephone
• Mobile
• Email
• Website URL
Nice to have
• Visual representation of tracking or maps.
Should not have
• Image of a satellite as currently shown

```html
<!DOCTYPE html>
<html lang="en">
<head>
<meta charset="utf-8">
<title>Lumen Rove – Business Card</title>
<link rel="stylesheet" href="https://fonts.googleapis.com/css2?family=Roboto:wght@400;500&display=swap">
<style>
  :root {
    --bg: #e9edf2;
    --card-blue: #0555a6;
    --brand-navy: #1c3a8c;
    --ink: #1a1a1a;
    --white: #ffffff;
    --map-sand: #eadfd3;
    --map-street: #f4f1ec;
    --map-water: #85acd3;
    --map-sky: #cfdeed;
    --route: #3a9b2f;
  }
  * { margin: 0; padding: 0; box-sizing: border-box; }
  html, body { width: 1200px; height: 900px; overflow: hidden; }
  body {
    background: var(--bg);
    font-family: "Roboto", Arial, sans-serif;
    display: flex;
    flex-direction: column;
    align-items: center;
    justify-content: center;
    gap: 40px;
  }
  .card {
    width: 680px;
    height: 389px;
    position: relative;
    overflow: hidden;
    box-shadow: 0 6px 18px rgba(0,0,0,.18);
  }

  /* Front */
  .card-front .map-area {
    position: absolute; inset: 0;
    background:
      radial-gradient(ellipse at 95% 10%, var(--map-sky) 0%, var(--map-water) 22%, transparent 40%),
      linear-gradient(135deg, var(--map-street) 0%, var(--map-sand) 50%, var(--map-street) 100%);
  }
  .brand-block {
    position: absolute;
    left: 0; right: 0;
    top: 150px;
    text-align: center;
  }
  .brand-name {
    display: inline-flex;
    align-items: center;
    gap: 12px;
    font-size: 46px;
    font-weight: 500;
    color: var(--brand-navy);
    letter-spacing: .5px;
  }
  .brand-dot {
    width: 18px; height: 18px;
    border-radius: 50%;
    background: var(--brand-navy);
  }
  .tagline {
    margin-top: 10px;
    font-size: 19px;
    font-weight: 500;
    color: var(--ink);
  }

  /* Back */
  .card-back { background: var(--card-blue); color: var(--white); }
  .identity {
    position: absolute;
    right: 400px;
    top: 148px;
    text-align: right;
  }
  .person-name { font-size: 22px; font-weight: 400; letter-spacing: .5px; }
  .person-title { font-size: 18px; margin-top: 2px; }
  .divider {
    position: absolute;
    left: 300px;
    top: 110px;
    width: 1px;
    height: 118px;
    background: var(--white);
  }
  .contacts {
    position: absolute;
    left: 320px;
    top: 112px;
    list-style: none;
    font-size: 17px;
    line-height: 28px;
  }
  .contacts li { display: flex; align-items: center; gap: 8px; }
  .contacts svg { width: 15px; height: 15px; flex: none; }
  .address {
    position: absolute;
    left: 0; right: 0;
    top: 268px;
    text-align: center;
    font-size: 19px;
  }
</style>
</head>
<body>
  <section class="card card-front">
    <div class="map-area" role="img" aria-label="Street map of a waterfront city with a green route line and coloured location pins"></div>
    <div class="brand-block">
      <div class="brand-name"><span class="brand-dot"></span>Lumen Rove</div>
      <p class="tagline">Premium Suppliers of Real Time Temperature Tracking</p>
    </div>
  </section>

  <section class="card card-back">
    <div class="identity">
      <p class="person-name">DALE MERCER</p>
      <p class="person-title">Managing Member</p>
    </div>
    <div class="divider"></div>
    <ul class="contacts">
      <li>
        <svg viewBox="0 0 16 16" aria-hidden="true"><rect x="0" y="0" width="16" height="16" rx="3" fill="#fff"/><path d="M5 3.5l2 2-1.2 1.3a6 6 0 0 0 3.4 3.4L10.5 9l2 2-1.3 1.5C7 12.5 3.5 9 3.5 4.8z" fill="#0555a6"/></svg>
        (555) 301-7270
      </li>
      <li>
        <svg viewBox="0 0 16 16" aria-hidden="true"><rect x="4" y="1" width="8" height="5" fill="#fff"/><rect x="1" y="6" width="14" height="6" rx="1" fill="#fff"/><rect x="4" y="10" width="8" height="5" fill="#fff" stroke="#0555a6" stroke-width="1"/></svg>
        (555) 301-6441
      </li>
      <li>
        <svg viewBox="0 0 16 16" aria-hidden="true"><rect x="1" y="3" width="14" height="10" fill="#fff"/><path d="M1 3l7 6 7-6" fill="none" stroke="#0555a6" stroke-width="1.3"/></svg>
        info@lumenrove.com
      </li>
      <li>
        <svg viewBox="0 0 16 16" aria-hidden="true" fill="none" stroke="#fff" stroke-width="1.2"><circle cx="8" cy="8" r="6.5"/><ellipse cx="8" cy="8" rx="3" ry="6.5"/><path d="M1.5 8h13"/></svg>
        www.lumenrove.com
      </li>
    </ul>
    <p class="address">418 Harbor Ridge Rd ste 210 Carlton, VIC 3053</p>
  </section>
</body>
</html>
```